【ワイヤーフレーム】
http://kovexa.hostmir.example/client-check/lumera/waiya.png
※極力ワイヤーフレームにそって作成して下さい。

【画像について】
各メニューに配置する写真とメインイメージの写真をお纏め致しました。
必ずこの写真を配置して下さい★
https://19.filevault.example/0827-3c7e1a9f40b2d65e8814a0c9f7d31b62

【今のサイトの問題点】
・何のメニューか分かりづらい
・鍼、カリオンの強みが弱い
・サイトからのお問い合わせが全くない

【TOPデザイン作成にあたっての要望】
・予約アイコンをつける
・ファイシャルメニューが一番売りたいメニューとなります。
デザインは目立つように作成して下さい。
・針、カリオン併用治療を押したい
・高級街にあるので高級感があるデザイン
・ピクセルノート、スナップロウのアイコンを配置する

【ターゲット】
・新規顧客さま
会社員、主婦、お金もっている30代~40代

【サイトの目的】
・集客
・店舗の強みの打ち出し

【サイトマップ】
①TOP
②ABOUT US スタッフ
③トータルビューティー
④フェイシャルビュティー
⑤インナービュティー
⑥コラーゲンマシーン
⑦遺伝子検査・腸内フローラ
⑧料金表
⑨メニュー内容
⑩ニュース一覧
⑪ニュース詳細
⑫ブログ一覧
⑬ブログ詳細
⑭鍼・カリオンの説明
⑮よくある質問
⑯アクセス、治療時間、お問い合わせ
⑰求人(非表示 ページには設けなくていいです)
⑱物販 (非表示 ページには設けなくていいです)
⑲実績
⑳お客様の声

【カラー】
・茶色
・グレー

【参考サイト】
https://www.velkanis.example/ https://moravel-co.example
https://www.lumera1954.example/
茶系、グレー系
【ワイヤーフレーム】
※極力ワイヤーフレームにそって作成して下さい。

【画像について】
必ずこの写真を配置して下さい★
暗めの印象で作成をお願い致します。
濃い色味7:明るい色味3
今回4日間だけ延長させて頂きます。

この度はたくさんの応募有難うございます。

またの機会に是非宜しくお願い致します!

```html
<!DOCTYPE html>
<html lang="ja">
<head>
<meta charset="utf-8">
<title>Lumera Life &amp; Beauty</title>
<link href="https://fonts.googleapis.com/css2?family=Noto+Serif+JP:wght@400;600;700&family=Cormorant+Garamond:wght@500;600&display=swap" rel="stylesheet">
<style>
:root{
  --brown-dark:#3e2518;
  --brown:#5a3522;
  --brown-mid:#7a4b32;
  --gold:#e3a83a;
  --gold-soft:#d9b46a;
  --gray:#9a9a9a;
  --gray-light:#d8d6d3;
  --cream:#f6f1ea;
  --white:#ffffff;
  --ink:#3a2a20;
}
*{margin:0;padding:0;box-sizing:border-box}
html,body{width:1200px;height:4568px;overflow:hidden}
body{font-family:"Noto Serif JP",serif;color:var(--ink);background:var(--white);position:relative}
.abs{position:absolute}
.photo{position:absolute}

/* hero */
.hero{position:absolute;left:0;top:0;width:1200px;height:680px;overflow:hidden}
.hero .photo{inset:0;background:linear-gradient(110deg,#6b4a35 0%,#b8896a 35%,#e8cbb0 60%,#a47455 100%)}
.logo{position:absolute;left:56px;top:52px;color:var(--brown-dark);font-family:"Cormorant Garamond",serif}
.logo .name{font-size:58px;font-weight:600;line-height:1}
.logo .sub{font-size:20px;margin-top:4px;padding-left:26px}
.logo .dot{display:inline-block;width:14px;height:14px;border:2px solid var(--brown-dark);border-radius:50%;margin-right:8px}
.social-top{position:absolute;right:24px;top:14px;display:flex;gap:12px}
.social-top span{width:40px;height:40px;background:var(--brown-dark)}
.catch{position:absolute;color:var(--brown-dark);font-weight:600}
.catch.l1{left:360px;top:320px;font-size:38px}
.catch.l2{left:180px;top:370px;font-size:40px}
.catch.kanji{left:300px;top:280px;font-size:130px;color:var(--gold);font-weight:700;line-height:1}
.catch.l3{left:440px;top:380px;font-size:38px}
.reserve{position:absolute;right:12px;width:92px;height:102px;background:var(--gold);border-radius:8px;display:flex;flex-direction:column;align-items:center;justify-content:center;gap:6px;font-size:15px;line-height:1.3;text-align:center;color:var(--brown-dark);border:2px solid #fff3}
.reserve.tel{top:270px}.reserve.web{top:490px}

/* nav */
.gnav{position:absolute;left:0;width:1200px;height:72px;display:flex;align-items:center;padding-left:14px;font-size:24px;color:var(--brown);letter-spacing:.5px}
.gnav.top{top:680px;background:var(--white)}
.gnav.bottom{top:4480px;height:60px;background:var(--brown-dark);color:var(--white);font-size:22px}
.copyright{position:absolute;top:4540px;left:0;width:1200px;height:28px;background:var(--brown-dark);color:#c9b6a8;font-size:12px;text-align:center}

/* menu */
.menus{position:absolute;top:752px;left:0;width:1200px;height:848px;background:var(--brown)}
.menu-title{position:absolute;color:var(--white);font-size:30px;letter-spacing:2px}
.menu-card{position:absolute}
.menu-card .photo{inset:0;background:linear-gradient(120deg,#5b3a28,#b68468 55%,#6e4732)}
.big-letter{position:absolute;font-family:"Cormorant Garamond",serif;color:var(--gold);line-height:1}
.big-letter b{font-size:130px;font-weight:600}
.big-letter span{font-size:80px;color:var(--white);font-weight:500}
.caption{position:absolute;font-size:20px;color:var(--white);text-align:center}
.caption.strong{color:var(--white);font-weight:600;font-size:24px;text-align:left}

/* intro */
.intro-heading{position:absolute;top:1700px;left:0;width:1200px;text-align:center;font-size:34px;color:var(--brown-dark);font-weight:600}
.pill{position:absolute;top:1790px;left:440px;width:320px;height:42px;border:2px solid var(--gold);border-radius:21px;text-align:center;line-height:38px;color:var(--gold);font-size:20px}
.diamond{position:absolute;width:150px;height:150px;transform:rotate(45deg);border:4px solid var(--gold-soft);overflow:hidden;background:linear-gradient(135deg,#e9d2bd,#b98a6b)}
.intro-text{position:absolute;font-size:26px;line-height:1.35;color:var(--ink)}
.more{position:absolute;top:2062px;left:0;width:1200px;text-align:center;font-size:26px}
.video{position:absolute;left:208px;top:2120px;width:772px;height:640px;background:var(--brown-mid);}
.video .photo{left:40px;top:40px;right:40px;bottom:40px;background:linear-gradient(140deg,#f1e0cf,#c9a085 60%,#8d5e44)}
.play{position:absolute;left:336px;top:270px}

/* voice */
.voice{position:absolute;top:2840px;left:0;width:1200px;height:320px;background:linear-gradient(90deg,#cfcac6,#eeebe8 50%,#c7c1bc)}
.voice h2{position:absolute;top:28px;width:1200px;text-align:center;font-family:"Cormorant Garamond",serif;font-size:40px;font-weight:500;color:var(--brown-dark);letter-spacing:4px}
.voice-box{position:absolute;width:220px;height:190px;background:var(--white);top:100px}
.voice-text{position:absolute;top:120px;font-size:22px;line-height:1.25;color:var(--ink)}

/* sns */
.sns{position:absolute;top:3200px;left:0;width:1200px;height:640px;background:var(--brown)}
.sns h2{position:absolute;top:10px;font-family:"Cormorant Garamond",serif;font-weight:500;font-size:44px;color:var(--gold-soft);letter-spacing:3px;display:flex;align-items:center;gap:12px}
.sns h2 i{display:inline-block;width:40px;height:40px;background:var(--gold)}
.feed-left{position:absolute;left:80px;top:220px;width:420px;height:340px;background:var(--white)}
.feed-left .photo{left:0;right:0;top:0;height:200px;background:linear-gradient(130deg,#c89a7c,#f0dccb 60%,#8b5b40)}
.feed-left .line{position:absolute;left:16px;height:12px;background:var(--gray-light)}
.insta{position:absolute;left:520px;top:80px;width:640px;height:540px;background:var(--white);padding:16px}
.insta .head{display:flex;align-items:center;gap:12px;font-size:22px;font-weight:600;color:var(--ink);height:56px;border-bottom:1px solid var(--gray-light)}
.insta .head i{width:38px;height:38px;border-radius:50%;background:var(--brown-mid)}
.grid{display:grid;grid-template-columns:repeat(3,1fr);gap:8px;margin-top:14px}
.grid div{height:104px;background:linear-gradient(135deg,#e5cdb6,#a97a5d)}
.grid div:nth-child(3n+2){background:linear-gradient(135deg,#d9d2c9,#8f7e70)}
.grid div:nth-child(4n){background:linear-gradient(135deg,#c04a3a,#ecc0a2)}

/* access */
.access-title{position:absolute;top:3880px;left:0;width:1200px;text-align:center;font-family:"Cormorant Garamond",serif;font-size:40px;color:var(--brown-dark);letter-spacing:4px}
.access-logo{position:absolute;left:140px;top:3960px;font-family:"Cormorant Garamond",serif;color:var(--brown-dark)}
.access-logo .name{font-size:40px;font-weight:600}
.access-info{position:absolute;left:60px;top:4040px;font-size:17px;line-height:1.6;color:var(--ink);width:460px}
.map{position:absolute;left:560px;top:3940px;width:600px;height:380px;background:linear-gradient(135deg,#eeeae2,#dfe5dc 50%,#eee7da)}
.btn{position:absolute;top:4352px;height:80px;background:var(--gray);color:var(--white);font-size:30px;display:flex;align-items:center;justify-content:center;gap:18px}
</style>
</head>
<body>

<header class="hero">
  <div class="photo" role="img" aria-label="施術ベッドで横になりリラックスする女性の写真"></div>
  <div class="logo"><div class="name">Lumera</div><div class="sub"><span class="dot"></span>Life &amp; Beauty</div></div>
  <div class="social-top"><span></span><span></span></div>
  <p class="catch l1">いているあなたに</p>
  <p class="catch kanji">輝</p>
  <p class="catch l2">もっと</p>
  <p class="catch l3">いてもらいたいという想いから</p>
  <a class="reserve tel">
    <svg width="34" height="34" viewBox="0 0 24 24"><path d="M6.6 10.8a15 15 0 006.6 6.6l2.2-2.2c.3-.3.7-.4 1-.2 1.1.4 2.3.6 3.6.6.6 0 1 .4 1 1V20c0 .6-.4 1-1 1A17 17 0 013 4c0-.6.4-1 1-1h3.5c.6 0 1 .4 1 1 0 1.3.2 2.5.6 3.6.1.3 0 .7-.2 1z" fill="#3e2518"/></svg>
    お電話<br>予約はこちら</a>
  <a class="reserve web">
    <svg width="36" height="30" viewBox="0 0 36 30"><rect x="5" y="3" width="26" height="18" fill="none" stroke="#3e2518" stroke-width="3"/><rect x="1" y="23" width="34" height="4" fill="#3e2518"/></svg>
    WEB<br>予約はこちら</a>
</header>

<nav class="gnav top">TOP／ABOUT US／鍼・カリオンとは／メニュー／お知らせ／ブログ／よくある質問／アクセス</nav>

<section class="menus">
  <h2 class="menu-title" style="left:60px;top:40px">フェイシャルビューティー</h2>
  <h2 class="menu-title" style="left:830px;top:50px">インナービューティー</h2>
  <div class="menu-card" style="left:56px;top:100px;width:552px;height:340px">
    <div class="photo" role="img" aria-label="フェイシャル施術を受ける女性の写真"></div>
    <div class="big-letter" style="left:6px;top:130px"><b>F</b><span>acial</span></div>
    <p class="caption strong" style="left:8px;top:300px">美容鍼とカリオンで内面から肌をきれいにしたい方</p>
  </div>
  <div class="menu-card" style="left:616px;top:100px;width:536px;height:260px">
    <div class="photo" role="img" aria-label="お腹に施術を受ける女性の写真"></div>
    <div class="big-letter" style="left:280px;top:120px"><b>I</b><span>nner</span></div>
  </div>
  <p class="caption" style="left:616px;top:368px;width:536px">体の表面の美しさを引き出したい方</p>

  <h2 class="menu-title" style="left:70px;top:490px;font-size:26px">トータルビューティー</h2>
  <h2 class="menu-title" style="left:500px;top:490px;font-size:26px">コラーゲンマシーン</h2>
  <h2 class="menu-title" style="left:900px;top:470px;font-size:24px;line-height:1.5">遺伝子検査<br>腸内フローラ検査</h2>

  <div class="menu-card" style="left:56px;top:540px;width:344px;height:240px">
    <div class="photo" role="img" aria-label="ベッドで施術を受ける女性の写真"></div>
    <div class="big-letter" style="left:8px;top:140px"><b style="font-size:100px">T</b><span style="font-size:64px">otal</span></div>
  </div>
  <p class="caption" style="left:56px;top:790px;width:344px">トータルで綺麗になりたい方</p>
  <div class="menu-card" style="left:416px;top:540px;width:364px;height:240px">
    <div class="photo" role="img" aria-label="赤い光のコラーゲンマシーンの写真" style="background:linear-gradient(120deg,#5a1c14,#d64a2e 50%,#7a2418)"></div>
  </div>
  <p class="caption" style="left:416px;top:790px;width:364px">体の中からキレイにしたい方</p>
  <div class="menu-card" style="left:796px;top:540px;width:356px;height:240px">
    <div class="photo" role="img" aria-label="お腹に手を当てる女性の写真" style="background:linear-gradient(120deg,#f3e2d4,#d6b19a 60%,#b58a70)"></div>
  </div>
</section>

<h2 class="intro-heading">美容鍼とカリオン筋膜美療器を同時に行う事ができる院です</h2>
<p class="pill">◆ 2つの相乗効果で可能に ◆</p>
<div class="diamond" style="left:125px;top:1880px" role="img" aria-label="顔に美容鍼を受ける女性の写真"></div>
<p class="intro-text" style="left:300px;top:1850px;width:270px">筋膜リリースでリンパ・血液が流れやすいスペースが生まれ、美容鍼で顔の筋肉を柔らかくする</p>
<p class="intro-text" style="left:590px;top:1850px;width:300px">更にコラーゲンの生成を促す事で小顔、リフトアップ効果の持続性を最大限に高める</p>
<div class="diamond" style="left:920px;top:1880px" role="img" aria-label="美容鍼の施術中の写真"></div>
<p class="more">↓ 詳しくはこちら ↓</p>

<div class="video">
  <div class="photo" role="img" aria-label="美容鍼の施術を紹介する動画のサムネイル"></div>
  <svg class="play" width="100" height="100" viewBox="0 0 100 100"><circle cx="50" cy="50" r="45" fill="none" stroke="#fff" stroke-width="6"/><path d="M40 30 L72 50 L40 70Z" fill="#fff"/></svg>
</div>

<section class="voice">
  <h2>VOICE</h2>
  <div class="voice-box" style="left:120px"></div>
  <p class="voice-text" style="left:400px">テキストテキスト<br>テキストテキスト<br>テキストテキスト<br>テキストテキスト<br>テキストテキスト<br>テキストテキスト</p>
  <div class="voice-box" style="left:670px"></div>
  <p class="voice-text" style="left:912px">テキストテキスト<br>テキストテキスト<br>テキストテキスト<br>テキストテキスト<br>テキストテキスト<br>テキストテキスト</p>
</section>

<section class="sns">
  <h2 style="left:120px">PIXELNOTE <i></i></h2>
  <h2 style="left:700px">SNAPROW <i></i></h2>
  <div class="feed-left">
    <div class="photo" role="img" aria-label="施術風景の投稿写真"></div>
    <div class="line" style="top:220px;width:300px"></div>
    <div class="line" style="top:248px;width:360px"></div>
    <div class="line" style="top:276px;width:240px"></div>
  </div>
  <div class="insta">
    <div class="head"><i></i>lumera.lab</div>
    <div class="grid" role="img" aria-label="投稿写真の一覧">
      <div></div><div></div><div></div><div></div><div></div><div></div>
      <div></div><div></div><div></div><div></div><div></div><div></div>
    </div>
  </div>
</section>

<h2 class="access-title">ACCESS</h2>
<div class="access-logo"><div class="name">Lumera</div></div>
<div class="access-info">
  東京都中央区銀座1-2-3 ルメラビル5F<br>
  <span style="font-size:13px;color:#777">最寄り駅から徒歩3分</span><br><br>
  03-5555-0198<br><br>
  受付時間<br>
  月曜〜金曜　11:00〜20:00<br>
  土日祝　10:00〜19:00
</div>
<div class="map" role="img" aria-label="店舗周辺の地図">
  <svg class="abs" style="left:260px;top:130px" width="40" height="56" viewBox="0 0 24 34"><path d="M12 0C5 0 0 5 0 12c0 9 12 22 12 22s12-13 12-22C24 5 19 0 12 0z" fill="#d93b2b"/><circle cx="12" cy="12" r="4.5" fill="#fff"/></svg>
</div>

<a class="btn" style="left:40px;width:480px">
  <svg width="34" height="34" viewBox="0 0 24 24"><path d="M6.6 10.8a15 15 0 006.6 6.6l2.2-2.2c.3-.3.7-.4 1-.2 1.1.4 2.3.6 3.6.6.6 0 1 .4 1 1V20c0 .6-.4 1-1 1A17 17 0 013 4c0-.6.4-1 1-1h3.5c.6 0 1 .4 1 1 0 1.3.2 2.5.6 3.6.1.3 0 .7-.2 1z" fill="#fff"/></svg>TEL予約</a>
<a class="btn" style="left:660px;width:500px">
  <svg width="40" height="32" viewBox="0 0 36 30"><rect x="5" y="3" width="26" height="18" fill="none" stroke="#fff" stroke-width="3"/><rect x="1" y="23" width="34" height="4" fill="#fff"/></svg>WEB予約</a>

<nav class="gnav bottom">TOP／ABOUT US／鍼・カリオンとは／メニュー／お知らせ／ブログ／よくある質問／アクセス</nav>
<p class="copyright">Copyright © Lumera Life &amp; Beauty All Rights Reserved.</p>

</body>
</html>
```